Visitenkarten-Design für Versicherungsmakler
Zielgruppe
Wir sind ein Versicherungsmakler aus Leipzig.
Aufgabenstellung
Im Anhang finden Sie die alte Visitenkarte. Die Daten können übernommen werden. Aber statt Inhaber bitte 'Geschäftsführer'
Die Farben sollten beibehalten werden. Bei der Frage ob das rot oder das grau die Primärfarbe ist, bin ich flexibel. Von der Gestaltung her sind Ihnen ansonsten keine Grenzen gesetzt.

```html
<!DOCTYPE html>
<html lang="de">
<head>
<meta charset="utf-8">
<title>valtera Finance Consulting – Visitenkarte</title>
<link rel="stylesheet" href="https://fonts.googleapis.com/css2?family=Raleway:ital,wght@0,400;0,500;0,600;1,500&display=swap">
<style>
  :root {
    --brand-red: #d4202a;
    --ink-grey: #4e4e4e;
    --band-light: #b3b3b5;
    --band-dark: #5a5a5c;
    --paper: #ffffff;
    --stage: #ffffff;
  }
  * { margin: 0; padding: 0; box-sizing: border-box; }
  html, body { width: 854px; height: 1200px; overflow: hidden; background: var(--stage); }
  body { position: relative; font-family: "Raleway", sans-serif; }

  .card {
    position: absolute;
    left: 102px;
    width: 648px;
    height: 420px;
    overflow: hidden;
  }
  .card--front { top: 86px; background: var(--paper); }
  .card--back { top: 606px; background: var(--brand-red); }

  .card__divider { position: absolute; inset: 0; width: 100%; height: 100%; }

  .brand-name {
    position: absolute;
    left: 38px; top: 24px;
    font-size: 68px; font-weight: 500;
    color: var(--brand-red);
    letter-spacing: 1px;
    line-height: 1;
  }
  .brand-tagline {
    position: absolute;
    left: 18px; top: 104px;
    font-size: 25px; font-weight: 500;
    color: var(--ink-grey);
    letter-spacing: 1.5px;
  }
  .person { position: absolute; left: 150px; top: 176px; width: 130px; text-align: center; color: var(--ink-grey); }
  .person__name { font-size: 18px; font-weight: 500; letter-spacing: 0.5px; white-space: nowrap; }
  .person__role { font-size: 12px; font-style: italic; font-weight: 500; margin-top: 4px; }

  .contact {
    position: absolute;
    right: 11px; top: 138px;
    text-align: right;
    color: var(--paper);
  }
  .contact__address { font-size: 17px; line-height: 18px; margin-bottom: 10px; }
  .contact__line { font-size: 15px; line-height: 21px; display: flex; justify-content: flex-end; align-items: center; gap: 6px; }
  .contact__line svg { width: 14px; height: 14px; fill: var(--paper); }
  .contact__mail { font-size: 12px; margin-top: 18px; }

  .legal {
    position: absolute;
    right: 11px; top: 322px;
    text-align: right;
    color: var(--paper);
    font-size: 12px; font-weight: 500;
    line-height: 16px;
    letter-spacing: 1px;
  }

  .web { position: absolute; right: 40px; top: 330px; color: var(--paper); text-align: right; }
  .web__icon { width: 32px; height: 32px; display: block; margin: 0 4px 12px auto; }
  .web__url { font-size: 22px; font-weight: 500; letter-spacing: 2.5px; }
</style>
</head>
<body>

<section class="card card--front" aria-label="Visitenkarte Vorderseite">
  <svg class="card__divider" viewBox="0 0 648 420" aria-hidden="true">
    <defs>
      <linearGradient id="band-gradient" x1="0" y1="0" x2="1" y2="0">
        <stop offset="0" stop-color="var(--band-light)"/>
        <stop offset="0.5" stop-color="#8d8d8f"/>
        <stop offset="1" stop-color="var(--band-dark)"/>
      </linearGradient>
    </defs>
    <path d="M0 262 C 250 250, 400 150, 648 0 L 648 420 L 0 420 Z" fill="url(#band-gradient)"/>
    <path d="M0 292 C 260 280, 420 180, 648 32 L 648 420 L 0 420 Z" fill="var(--brand-red)"/>
  </svg>

  <div class="brand-name">valtera</div>
  <div class="brand-tagline">FINANCE CONSULTING</div>

  <div class="person">
    <div class="person__name">LARS BRENNER</div>
    <div class="person__role">Geschäftsführer</div>
  </div>

  <div class="contact">
    <div class="contact__address">Birkenauer Weg<br>48&nbsp;&nbsp;04177 Leipzig</div>
    <div class="contact__line">
      <svg viewBox="0 0 24 24"><path d="M6.6 10.8a15 15 0 0 0 6.6 6.6l2.2-2.2c.3-.3.7-.4 1-.2 1.1.4 2.3.6 3.6.6.6 0 1 .4 1 1V20c0 .6-.4 1-1 1A17 17 0 0 1 3 4c0-.6.4-1 1-1h3.5c.6 0 1 .4 1 1 0 1.3.2 2.5.6 3.6.1.3 0 .7-.2 1z"/></svg>
      <span>Tel: 0341-55102736</span>
    </div>
    <div class="contact__line">
      <svg viewBox="0 0 24 24"><path d="M7 1h10a2 2 0 0 1 2 2v18a2 2 0 0 1-2 2H7a2 2 0 0 1-2-2V3a2 2 0 0 1 2-2zm0 3v13h10V4zm5 15a1.2 1.2 0 1 0 0 2.4 1.2 1.2 0 0 0 0-2.4z"/></svg>
      <span>Mobil: 0176-402 81 93.</span>
    </div>
    <div class="contact__line">
      <svg viewBox="0 0 24 24"><path d="M3 6h4v16H3zm6 2h12v14H9zm2 2v3h8v-3zm0 5v2h2v-2zm3 0v2h2v-2zm3 0v2h2v-2zm-6 3v2h2v-2zm3 0v2h2v-2zm3 0v2h2v-2zM9 2h8v4H9z"/></svg>
      <span>Fax: 0341-55102739</span>
    </div>
    <div class="contact__line contact__mail">
      <svg viewBox="0 0 24 24"><path d="M2 5h20v14H2zm2 2v.4l8 5 8-5V7zm0 2.8V17h16V9.8l-8 5z"/></svg>
      <span>lars.brenner@valtera.de</span>
    </div>
  </div>

  <div class="legal">
    Freier Versicherungsmakler<br>
    mit Erlaubnis nach § 34d Abs. 1 GewO -<br>
    Erlaubnisbehörde:<br>
    Kammer Elstertal,Lindenplatz 12,<br>
    04103 Leipzig - Reg.-Nr.D-4KRT-M71PQ-20
  </div>
</section>

<section class="card card--back" aria-label="Visitenkarte Rückseite">
  <div class="web">
    <svg class="web__icon" viewBox="0 0 32 32" aria-hidden="true" fill="none" stroke="var(--paper)" stroke-width="1.8">
      <circle cx="16" cy="16" r="14"/>
      <ellipse cx="16" cy="16" rx="6" ry="14"/>
      <line x1="2" y1="16" x2="30" y2="16"/>
      <line x1="5" y1="9" x2="27" y2="9"/>
      <line x1="5" y1="23" x2="27" y2="23"/>
    </svg>
    <div class="web__url">www.valtera.de</div>
  </div>
</section>

</body>
</html>
```